New shirt company looking for a fun and edgy online retail website design

We're a new company looking for a simple yet attractive website to sell shirts/tops to a mostly younger female audience. Our name is Tilvo Shirt Co. and the ArtPavilion logo is uploaded. We're thinking a home page, three separate pages for our shirt "collections", and a contact page/cart page for a grand total of 5 pages. We'd like the website to be coded, easy for the consumer to navigate/shop/checkout, and easy to link to various social media platforms and online websites. For colors, we're aiming for various blues, light grey, and maybe tan/khaki. Our goal is to launch with approximately 20-30 tops/shirts (or 7-10) per page. Please let us know if you have any questions and thank you for helping us! We are very excited to see what is created!

Target Market(s)

Female teens to early twenties

Coding

Coded - Design and coding required

Number of Pages Required

3 page

Font styles to use
Decorative
Script

Colors
cee9f5
85cae6
33a6d7
0393ce
cfdfed
85acd3

Requirements
Must have
• Online shopping/purchasing capabilities, dropdowns to select sizes for each item, easy to add/remove new or seasoned items.

```html
<!DOCTYPE html>
<html lang="en">
<head>
<meta charset="utf-8">
<title>Tilvo Shirt Co. — Home</title>
<link rel="stylesheet" href="https://fonts.googleapis.com/css2?family=Montserrat:wght@400;500;600;700&family=Roboto:wght@400;500&display=swap">
<style>
:root{
  --blue:#33a6d7;
  --blue-deep:#0393ce;
  --blue-soft:#85cae6;
  --blue-pale:#cee9f5;
  --logo-bg:#6bb8dc;
  --ink:#111;
  --text:#333;
  --muted:#666;
  --grey:#ebebeb;
  --foot:#efefef;
  --line:#d6d6d6;
  --star:#f2c200;
}
*{box-sizing:border-box;margin:0;padding:0}
html,body{width:1200px;height:4337px;overflow:hidden;background:#fff}
body{position:relative;font-family:"Roboto",sans-serif;color:var(--text)}
.abs{position:absolute}
h1,h2,h3,.mont{font-family:"Montserrat",sans-serif}

/* header */
.site-header{position:absolute;left:0;top:0;width:1200px;height:88px;background:#fff}
.brand{position:absolute;left:88px;top:0;width:178px;height:88px;background:var(--logo-bg);display:flex;align-items:center;justify-content:center;font-family:"Montserrat",sans-serif;font-weight:600;font-size:26px;color:#fff}
.nav{position:absolute;top:30px;left:452px;display:flex;gap:0;font-family:"Montserrat",sans-serif;font-weight:500;font-size:16px;color:var(--ink)}
.nav a{color:inherit;text-decoration:none;position:absolute;white-space:nowrap}
.nav a.active{color:var(--blue)}

/* hero */
.hero{position:absolute;left:0;top:88px;width:1200px;height:580px;background:var(--blue)}
.hero-photo{position:absolute;right:0;top:0;width:645px;height:580px;background:linear-gradient(100deg,var(--blue) 0%,#e9c8c0 30%,#7d8494 60%,#2f7fb0 100%)}
.hero h1{position:absolute;left:89px;top:140px;font-size:82px;font-weight:600;color:#fff;letter-spacing:1px;line-height:1}
.hero .sub{position:absolute;left:89px;top:228px;font-family:"Montserrat",sans-serif;font-weight:500;font-size:36px;color:#fff}
.hero p{position:absolute;left:89px;top:292px;width:480px;font-family:"Montserrat",sans-serif;font-size:21px;line-height:27px;color:#fff}
.btn-buy{position:absolute;left:89px;top:378px;width:146px;height:40px;border-radius:20px;background:#fff;color:var(--blue);font-family:"Montserrat",sans-serif;font-weight:500;font-size:16px;display:flex;align-items:center;justify-content:center}

/* categories */
.cat{position:absolute;top:772px;width:496px;height:383px;display:flex;align-items:center;justify-content:center;gap:14px;font-family:"Montserrat",sans-serif;font-weight:600;font-size:32px;color:#fff}
.cat .arrow{width:44px;height:44px;border-radius:50%;background:var(--blue-soft);display:flex;align-items:center;justify-content:center}

/* sale */
.sale{position:absolute;left:89px;top:1257px;width:1022px;height:434px;background:linear-gradient(90deg,#3a3634,#2b2a2c 45%,#3d4048 70%,#4a4a4a)}
.sale h2{position:absolute;left:0;width:100%;top:96px;text-align:center;font-weight:500;font-size:40px;color:#fff}
.feature{position:absolute;top:170px;width:240px;text-align:center;color:#fff}
.feature svg{display:block;margin:0 auto 12px}
.feature h3{font-weight:600;font-size:16px;margin-bottom:14px}
.feature p{font-size:13px;line-height:22px}

/* products */
.section-title{position:absolute;left:0;width:1200px;text-align:center;font-family:"Montserrat",sans-serif;font-weight:500;font-size:42px;color:var(--ink)}
.product{position:absolute;width:244px}
.product .photo{height:256px}
.product h3{margin-top:12px;font-weight:600;font-size:22px;color:var(--ink);line-height:26px}
.product .desc{font-size:14px;color:var(--muted);line-height:18px}
.product hr{border:0;border-top:2px solid var(--line);margin-top:9px}
.product .row{display:flex;justify-content:space-between;align-items:center;margin-top:8px;font-size:16px;color:#444}
.cart{width:30px;height:30px;border-radius:50%;background:#d0d0d0;display:flex;align-items:center;justify-content:center}

/* offers */
.offers{position:absolute;left:0;top:2743px;width:1200px;height:733px;background:var(--grey)}
.offer{position:absolute;font-family:"Montserrat",sans-serif}
.offer .link{font-size:15px;text-decoration:underline}

/* testimonials */
.stars{position:absolute;left:0;width:1200px;top:3636px;text-align:center;color:var(--star);font-size:20px;letter-spacing:6px}
.quote{position:absolute;left:130px;width:940px;top:3672px;text-align:center;font-size:14px;line-height:27px;color:#444}
.avatar{position:absolute;border-radius:50%}

/* footer */
.site-footer{position:absolute;left:0;top:4007px;width:1200px;height:330px;background:var(--foot);font-size:14px;color:#444}
.fcol{position:absolute;top:76px;line-height:28.6px}
.fcol div{display:flex;align-items:center;gap:10px}
.pay{display:grid;grid-template-columns:repeat(4,34px);gap:10px 6px;position:absolute;left:958px;top:84px}
.pay span{height:20px;border-radius:3px}
.copy{position:absolute;left:0;width:1200px;top:288px;text-align:center;font-size:12px;color:#777}
</style>
</head>
<body>

<header class="site-header">
  <div class="brand">Tilvo</div>
  <nav class="nav">
    <a class="active" style="left:0">Home</a>
    <a style="left:96px">About Us</a>
    <a style="left:216px">Products</a>
    <a style="left:333px">Collections</a>
    <a style="left:467px">Gallery</a>
    <a style="left:569px">Contact Us</a>
  </nav>
</header>

<section class="hero">
  <div class="hero-photo" role="img" aria-label="Stylish couple in sunglasses posing against a blue wall"></div>
  <h1>TILVO</h1>
  <div class="sub">Shirt Company</div>
  <p>Lorem ipsum dolor sit amet, consectetur adipiscing elit, sed do eiusmod</p>
  <div class="btn-buy">Buy Now</div>
</section>

<a class="cat" style="left:91px;background:linear-gradient(135deg,#3a3c48,#2f4a7a 55%,#55586a)" role="img" aria-label="Smiling man in a denim shirt">Men <span class="arrow"><svg width="16" height="16" viewBox="0 0 16 16"><path d="M3 8h9M8 4l4 4-4 4" stroke="#fff" stroke-width="2.2" fill="none"/></svg></span></a>
<a class="cat" style="left:613px;background:linear-gradient(135deg,#6a6a6a,#3a3a3a 55%,#7a7a7a)" role="img" aria-label="Woman in a checked coat against a concrete wall">Women <span class="arrow"><svg width="16" height="16" viewBox="0 0 16 16"><path d="M3 8h9M8 4l4 4-4 4" stroke="#fff" stroke-width="2.2" fill="none"/></svg></span></a>

<section class="sale" role="img" aria-label="Dark photo of a couple in patterned and jacket outfits">
  <h2>Sale for this starts in</h2>
  <div class="feature" style="left:81px">
    <svg width="60" height="40" viewBox="0 0 60 40" fill="none" stroke="#fff" stroke-width="1.8"><rect x="14" y="6" width="26" height="22"/><path d="M40 14h10l6 8v6H40z"/><circle cx="22" cy="31" r="4"/><circle cx="48" cy="31" r="4"/><path d="M2 14h9M5 20h6"/></svg>
    <h3>Two Days Shipping</h3>
    <p>Lorem ipsum dolor sit amet, consectetur adipiscing elit, sed do eiusmod tempor incididunt</p>
  </div>
  <div class="feature" style="left:390px">
    <svg width="60" height="40" viewBox="0 0 60 40" fill="none" stroke="#fff" stroke-width="1.8"><circle cx="34" cy="16" r="12"/><path d="M34 9v14M30 12h6a2 2 0 010 4h-4a2 2 0 000 4h6"/><path d="M6 32h12l10 4 18-6"/></svg>
    <h3>30 Days Money Back</h3>
    <p>Lorem ipsum dolor sit amet, consectetur adipiscing elit, sed do eiusmod tempor incididunt</p>
  </div>
  <div class="feature" style="left:700px">
    <svg width="60" height="40" viewBox="0 0 60 40" fill="none" stroke="#fff" stroke-width="1.8"><circle cx="30" cy="20" r="16"/><ellipse cx="30" cy="20" rx="7" ry="16"/><path d="M14 20h32M17 12h26M17 28h26"/></svg>
    <h3>Worldwide shipping</h3>
    <p>Lorem ipsum dolor sit amet, consectetur adipiscing elit, sed do eiusmod tempor incididunt</p>
  </div>
</section>

<h2 class="section-title" style="top:1782px">Check Out What’s New</h2>

<div class="product" style="left:89px;top:1858px"><div class="photo" role="img" aria-label="Man in a white button-up shirt" style="background:linear-gradient(180deg,#f2f2f2,#dfe3ea)"></div><h3>Product Name</h3><div class="desc">Lorem ipsum</div><hr><div class="row">$50.00<span class="cart"><svg width="14" height="14" viewBox="0 0 14 14"><path d="M1 2h2l2 7h6l2-5H4" fill="#33a6d7"/><circle cx="6" cy="12" r="1.3" fill="#33a6d7"/><circle cx="11" cy="12" r="1.3" fill="#33a6d7"/></svg></span></div></div>
<div class="product" style="left:348px;top:1858px"><div class="photo" role="img" aria-label="Woman in a grey t-shirt" style="background:linear-gradient(180deg,#eeeae6,#a9a9a9)"></div><h3>Product Name</h3><div class="desc">Lorem ipsum</div><hr><div class="row">$50.00<span class="cart"><svg width="14" height="14" viewBox="0 0 14 14"><path d="M1 2h2l2 7h6l2-5H4" fill="#33a6d7"/><circle cx="6" cy="12" r="1.3" fill="#33a6d7"/><circle cx="11" cy="12" r="1.3" fill="#33a6d7"/></svg></span></div></div>
<div class="product" style="left:607px;top:1858px"><div class="photo" role="img" aria-label="Man in a white shirt with arms crossed" style="background:linear-gradient(180deg,#f4f4f4,#c9ccd6 80%,#2c3a5a)"></div><h3>Product Name</h3><div class="desc">Lorem ipsum</div><hr><div class="row">$50.00<span class="cart"><svg width="14" height="14" viewBox="0 0 14 14"><path d="M1 2h2l2 7h6l2-5H4" fill="#33a6d7"/><circle cx="6" cy="12" r="1.3" fill="#33a6d7"/><circle cx="11" cy="12" r="1.3" fill="#33a6d7"/></svg></span></div></div>
<div class="product" style="left:867px;top:1858px"><div class="photo" role="img" aria-label="Woman in a striped t-shirt holding a phone" style="background:linear-gradient(180deg,#a9a6a1,#6f6f70)"></div><h3>Product Name</h3><div class="desc">Lorem ipsum</div><hr><div class="row">$50.00<span class="cart"><svg width="14" height="14" viewBox="0 0 14 14"><path d="M1 2h2l2 7h6l2-5H4" fill="#33a6d7"/><circle cx="6" cy="12" r="1.3" fill="#33a6d7"/><circle cx="11" cy="12" r="1.3" fill="#33a6d7"/></svg></span></div></div>

<div class="product" style="left:89px;top:2269px"><div class="photo" role="img" aria-label="Woman in a denim shirt" style="background:linear-gradient(180deg,#e6e6e6,#7ea0c4)"></div><h3>Product Name</h3><div class="desc">Lorem ipsum</div><hr><div class="row">$50.00<span class="cart"><svg width="14" height="14" viewBox="0 0 14 14"><path d="M1 2h2l2 7h6l2-5H4" fill="#33a6d7"/><circle cx="6" cy="12" r="1.3" fill="#33a6d7"/><circle cx="11" cy="12" r="1.3" fill="#33a6d7"/></svg></span></div></div>
<div class="product" style="left:348px;top:2269px"><div class="photo" role="img" aria-label="Man in a plaid shirt" style="background:linear-gradient(180deg,#eeeeee,#6a4a5a 50%,#2c3b58)"></div><h3>Product Name</h3><div class="desc">Lorem ipsum</div><hr><div class="row">$50.00<span class="cart"><svg width="14" height="14" viewBox="0 0 14 14"><path d="M1 2h2l2 7h6l2-5H4" fill="#33a6d7"/><circle cx="6" cy="12" r="1.3" fill="#33a6d7"/><circle cx="11" cy="12" r="1.3" fill="#33a6d7"/></svg></span></div></div>
<div class="product" style="left:607px;top:2269px"><div class="photo" role="img" aria-label="Woman in a white lace camisole" style="background:linear-gradient(180deg,#c9a070,#f2f2f2 60%,#5a4a40)"></div><h3>Product Name</h3><div class="desc">Lorem ipsum</div><hr><div class="row">$50.00<span class="cart"><svg width="14" height="14" viewBox="0 0 14 14"><path d="M1 2h2l2 7h6l2-5H4" fill="#33a6d7"/><circle cx="6" cy="12" r="1.3" fill="#33a6d7"/><circle cx="11" cy="12" r="1.3" fill="#33a6d7"/></svg></span></div></div>
<div class="product" style="left:867px;top:2269px"><div class="photo" role="img" aria-label="Man jumping in a patterned shirt and orange trousers" style="background:linear-gradient(180deg,#f0f0f0,#d8d8d8 55%,#c4622a)"></div><h3>Product Name</h3><div class="desc">Lorem ipsum</div><hr><div class="row">$50.00<span class="cart"><svg width="14" height="14" viewBox="0 0 14 14"><path d="M1 2h2l2 7h6l2-5H4" fill="#33a6d7"/><circle cx="6" cy="12" r="1.3" fill="#33a6d7"/><circle cx="11" cy="12" r="1.3" fill="#33a6d7"/></svg></span></div></div>

<section class="offers">
  <h2 class="section-title" style="top:94px">Best Offers</h2>
  <div class="offer" style="left:89px;top:164px;width:525px;height:469px;background:linear-gradient(180deg,#4a4a4c,#5b4636 60%,#8a6a48)" role="img" aria-label="Couple in winter jackets sitting on a wooden pallet bench">
    <div style="position:absolute;left:14px;top:8px;color:#fff;font-weight:600;font-size:28px;letter-spacing:3px;line-height:38px">Get<br><span style="font-size:46px;font-weight:700;line-height:54px">25%</span><br>Offer</div>
    <div class="link" style="position:absolute;left:16px;top:152px;color:#fff">Buy Now</div>
  </div>
  <div class="offer" style="left:624px;top:164px;width:487px;height:227px;background:linear-gradient(90deg,#a8a29c,#8d8782 55%,#e6b020 75%,#9a948f)" role="img" aria-label="Woman in a yellow top">
    <div style="position:absolute;left:20px;top:16px;color:#fff;font-size:23px;line-height:33px">Get <b>40%</b> Off<br>in Women Top</div>
    <div class="link" style="position:absolute;left:21px;top:110px;color:#fff">Buy Now</div>
  </div>
  <div class="offer" style="left:624px;top:406px;width:487px;height:227px;background:linear-gradient(90deg,#cfd0d8,#6c7aa0 40%,#cfd3de 75%)" role="img" aria-label="Smiling man in a blue shirt">
    <div style="position:absolute;left:307px;top:36px;color:#444;font-size:23px;line-height:33px">Get <b>40%</b> Off<br>in Men Shirt</div>
    <div class="link" style="position:absolute;left:308px;top:130px;color:#444">Buy Now</div>
  </div>
</section>

<h2 class="section-title" style="top:3568px">Testimonials</h2>
<div class="stars">★★★★★</div>
<p class="quote">Lorem ipsum dolor sit amet, consectetur adipiscing elit, sed do eiusmod tempor incididunt ut labore et dolore magna aliqua. Ut enim ad minim veniam, quis nostrud exercitation ullamco laboris nisi ut aliquip ex ea commodo consequat.</p>
<svg class="abs" style="left:278px;top:3800px" width="16" height="20" viewBox="0 0 16 20"><path d="M11 3L4 10l7 7" stroke="#333" stroke-width="2.5" fill="none"/></svg>
<svg class="abs" style="left:906px;top:3800px" width="16" height="20" viewBox="0 0 16 20"><path d="M5 3l7 7-7 7" stroke="#333" stroke-width="2.5" fill="none"/></svg>
<div class="avatar" style="left:399px;top:3763px;width:94px;height:94px;background:#e2d6e4" role="img" aria-label="Customer portrait"></div>
<div class="avatar" style="left:544px;top:3755px;width:110px;height:110px;background:linear-gradient(180deg,#5a4034,#c89a84)" role="img" aria-label="Customer portrait"></div>
<div class="avatar" style="left:704px;top:3763px;width:94px;height:94px;background:#e2d6e4" role="img" aria-label="Customer portrait"></div>
<div class="abs" style="left:0;width:1200px;top:3883px;text-align:center;font-size:17px;color:#444">M. Dorsan</div>

<footer class="site-footer">
  <div class="fcol" style="left:155px"><div>Home</div><div>About Us</div><div>Products</div><div>Collections</div><div>Gallery</div><div>Contact Us</div></div>
  <div class="fcol" style="left:406px"><div>Privacy Policy</div><div>Faq</div><div>Terms &amp; Conditions</div></div>
  <div class="fcol" style="left:687px">
    <div><span style="width:8px;height:8px;background:#333;border-radius:50%"></span>Circlebook</div>
    <div><span style="width:8px;height:8px;background:#333;border-radius:50%"></span>Chirper</div>
    <div><span style="width:8px;height:8px;background:#333;border-radius:50%"></span>Snapgram</div>
    <div><span style="width:8px;height:8px;background:#333;border-radius:50%"></span>Workedin</div>
  </div>
  <div class="pay">
    <span style="background:#2e77bc"></span><span style="background:#fff;border:1px solid #bbb"></span><span style="background:#fff;border:1px solid #ccc"></span><span></span>
    <span style="background:#fff;border:1px solid #ddd"></span><span style="background:#fff;border:1px solid #ddd"></span><span style="background:#5a31f4"></span><span style="background:#fff;border:1px solid #ddd"></span>
  </div>
  <div class="copy">Copyright © 2020 The Company Name.All rights reserved.</div>
</footer>

</body>
</html>
```